8 x 8 Social Media Design - Tax, Accounting & Bookkeeping Service

Bright Ledger Advisory Group, Inc.

Tax, Accounting and Bookkeeping Services

“We provide our services, with you next mortgage in mind”

Special pricing available for all Mortgage Loan Customers!!

President / CEO Marcus Delaney

Primary service provider with over 27 years of experience

Call directly for more information: (555) 284-9037

Or email at: mdelaney@brightledgerhq.example

```html
<!DOCTYPE html>
<html lang="en">
<head>
<meta charset="utf-8">
<title>Bright Ledger Advisory Group – Tax, Accounting and Bookkeeping Services</title>
<link href="https://fonts.googleapis.com/css2?family=Bebas+Neue&family=Montserrat:ital,wght@0,400;0,500;0,600;0,700;0,800;1,500;1,800&display=swap" rel="stylesheet">
<style>
  :root {
    --backdrop: #d4d4d4;
    --ink: #050505;
    --white: #ffffff;
    --gold: #e2a93a;
    --gold-light: #f4c965;
    --gold-deep: #b17a1c;
    --blue: #1d44a6;
    --blue-deep: #0f2a78;
    --navy: #10183a;
  }
  * { margin: 0; padding: 0; box-sizing: border-box; }
  html, body { width: 1200px; height: 2430px; overflow: hidden; }
  body { background: var(--backdrop); position: relative; font-family: "Montserrat", sans-serif; }

  .social-post {
    position: absolute; left: 0; top: 1230px; width: 1200px; height: 1200px;
    background: var(--ink); overflow: hidden; color: var(--white);
  }
  .social-post.is-preview {
    left: 90px; top: 105px; transform: scale(0.85); transform-origin: top left;
    box-shadow: 0 24px 40px rgba(0,0,0,.35);
  }

  /* ---------- upper panel ---------- */
  .light-streaks {
    position: absolute; left: 0; top: 0; width: 1200px; height: 700px;
    background:
      radial-gradient(ellipse 420px 160px at 720px 150px, rgba(240,170,50,.75), transparent 70%),
      radial-gradient(ellipse 520px 120px at 880px 330px, rgba(220,140,30,.55), transparent 72%),
      linear-gradient(160deg, transparent 25%, rgba(200,120,20,.35) 45%, transparent 65%);
  }
  .portrait {
    position: absolute; left: 770px; top: 50px; width: 420px; height: 620px;
    background: linear-gradient(180deg, #1a1a1f 0%, #24252c 45%, #121318 100%);
    border-radius: 200px 200px 0 0;
  }
  .brand { position: absolute; left: 38px; top: 120px; display: flex; align-items: center; gap: 16px; }
  .brand-dot { width: 34px; height: 34px; border-radius: 50%; background: var(--gold); flex: none; }
  .brand-name { font-weight: 700; font-size: 30px; line-height: 1.15; color: var(--gold); width: 360px; }
  .headline {
    position: absolute; left: 38px; top: 292px; white-space: nowrap;
    font-family: "Bebas Neue", sans-serif; font-weight: 400; font-size: 128px; line-height: 110px;
    color: var(--white); transform: scaleX(0.8); transform-origin: left top;
    text-shadow: 0 0 14px rgba(255,230,170,.55);
  }
  .motto {
    position: absolute; left: 38px; top: 548px; width: 595px; height: 84px;
    background: var(--blue); border-radius: 42px;
    color: var(--gold); font-weight: 600; font-size: 32px; line-height: 36px;
    text-align: center; padding-top: 6px;
  }
  .name-plate {
    position: absolute; left: 640px; top: 548px; width: 465px; height: 84px;
    background: linear-gradient(90deg, transparent 0%, var(--gold-deep) 12%, var(--gold) 55%, var(--gold-light) 100%);
    color: var(--navy); text-align: center; padding-top: 5px;
  }
  .name-plate .person { font-weight: 800; font-size: 34px; line-height: 38px; }
  .name-plate .role { font-weight: 500; font-size: 28px; letter-spacing: 4px; line-height: 34px; }
  .swoosh { position: absolute; left: 0; top: 0; width: 1200px; height: 760px; }

  /* ---------- lower panel ---------- */
  .family-photo {
    position: absolute; left: 0; top: 700px; width: 560px; height: 480px;
    background: linear-gradient(120deg, #cfc7bd 0%, #8e7a66 45%, #3a2f27 80%, #0a0a0a 100%);
  }
  .experience {
    position: absolute; right: 40px; top: 733px; text-align: right;
    font-weight: 500; font-size: 56px; line-height: 58px; color: var(--white);
  }
  .experience strong { font-weight: 800; }
  .rule { position: absolute; right: 40px; height: 2px; background: linear-gradient(90deg, transparent, var(--gold)); }
  .rule.one { top: 944px; width: 900px; }
  .rule.two { top: 1064px; width: 780px; }
  .offer { position: absolute; right: 40px; top: 948px; text-align: right; }
  .offer .lead { font-weight: 500; font-size: 42px; color: var(--gold); line-height: 50px; }
  .offer .audience { font-weight: 800; font-style: italic; font-size: 48px; line-height: 58px; }
  .contact-intro {
    position: absolute; left: 38px; top: 1076px;
    font-style: italic; font-weight: 500; font-size: 25px; line-height: 30px;
  }
  .contact-line {
    position: absolute; top: 1114px; height: 46px; display: flex; align-items: center; gap: 12px;
    color: var(--gold); font-weight: 700; line-height: 46px; white-space: nowrap;
  }
  .contact-line.phone { left: 38px; font-size: 36px; }
  .contact-line.email { right: 40px; font-size: 32px; font-weight: 500; }
  .contact-line svg { flex: none; }
  .base-band { position: absolute; left: 0; bottom: 0; width: 1200px; height: 20px; background: var(--blue); }
</style>
</head>
<body>
  <section class="social-post is-preview" aria-hidden="true">
    <div class="light-streaks"></div>
    <div class="portrait"></div>
    <svg class="swoosh" viewBox="0 0 1200 760">
      <path d="M1200 330 C1180 520 1120 600 960 650 L0 670 L0 700 L960 690 C1120 670 1200 560 1200 470 Z" fill="var(--blue)"/>
      <path d="M1200 470 C1190 600 1100 680 900 700 L0 702 L0 700 L960 690 C1120 670 1200 560 1200 470 Z" fill="var(--blue-deep)"/>
    </svg>
    <div class="brand"><span class="brand-dot"></span><span class="brand-name">Bright Ledger Advisory Group, Inc.</span></div>
    <p class="headline">TAX, ACCOUNTING AND<br>BOOKKEEPING SERVICES</p>
    <p class="motto">We provide our services,<br>with you next mortgage in mind</p>
    <div class="name-plate"><div class="person">MARCUS DELANEY</div><div class="role">PRESIDENT / CEO</div></div>
    <div class="family-photo"></div>
    <p class="experience">PRIMARY SERVICE PROVIDER<br>WITH OVER <strong>27 YEARS</strong><br>OF EXPERIENCE</p>
    <div class="rule one"></div>
    <div class="offer"><p class="lead">Special pricing available for all</p><p class="audience">Mortgage Loan Customers!!</p></div>
    <div class="rule two"></div>
    <p class="contact-intro">Directly for more information</p>
    <p class="contact-line phone">
      <svg width="30" height="30" viewBox="0 0 24 24"><path fill="#fff" d="M6.6 10.8a15.1 15.1 0 0 0 6.6 6.6l2.2-2.2c.3-.3.7-.4 1-.2 1.1.4 2.3.6 3.6.6.6 0 1 .4 1 1V20c0 .6-.4 1-1 1A17 17 0 0 1 3 4c0-.6.4-1 1-1h3.5c.6 0 1 .4 1 1 0 1.3.2 2.5.6 3.6.1.3 0 .7-.2 1z"/></svg>
      (555) 284-9037
    </p>
    <p class="contact-line email">
      <svg width="34" height="24" viewBox="0 0 34 24"><rect x="1" y="1" width="32" height="22" fill="#fff"/><path d="M1 1 L17 14 L33 1" fill="none" stroke="#050505" stroke-width="2"/></svg>
      mdelaney@brightledgerhq.example
    </p>
    <div class="base-band"></div>
  </section>

  <main class="social-post">
    <div class="light-streaks" role="img" aria-label="Golden light streaks with sparkles across a black background"></div>
    <div class="portrait" role="img" aria-label="Portrait of the company president in a dark hat and coat"></div>
    <svg class="swoosh" viewBox="0 0 1200 760" aria-hidden="true">
      <path d="M1200 330 C1180 520 1120 600 960 650 L0 670 L0 700 L960 690 C1120 670 1200 560 1200 470 Z" fill="var(--blue)"/>
      <path d="M1200 470 C1190 600 1100 680 900 700 L0 702 L0 700 L960 690 C1120 670 1200 560 1200 470 Z" fill="var(--blue-deep)"/>
    </svg>
    <div class="brand"><span class="brand-dot"></span><span class="brand-name">Bright Ledger Advisory Group, Inc.</span></div>
    <h1 class="headline">TAX, ACCOUNTING AND<br>BOOKKEEPING SERVICES</h1>
    <p class="motto">We provide our services,<br>with you next mortgage in mind</p>
    <div class="name-plate"><div class="person">MARCUS DELANEY</div><div class="role">PRESIDENT / CEO</div></div>
    <div class="family-photo" role="img" aria-label="Happy couple unpacking moving boxes in their new home"></div>
    <p class="experience">PRIMARY SERVICE PROVIDER<br>WITH OVER <strong>27 YEARS</strong><br>OF EXPERIENCE</p>
    <div class="rule one"></div>
    <div class="offer"><p class="lead">Special pricing available for all</p><p class="audience">Mortgage Loan Customers!!</p></div>
    <div class="rule two"></div>
    <p class="contact-intro">Directly for more information</p>
    <p class="contact-line phone">
      <svg width="30" height="30" viewBox="0 0 24 24" aria-hidden="true"><path fill="#fff" d="M6.6 10.8a15.1 15.1 0 0 0 6.6 6.6l2.2-2.2c.3-.3.7-.4 1-.2 1.1.4 2.3.6 3.6.6.6 0 1 .4 1 1V20c0 .6-.4 1-1 1A17 17 0 0 1 3 4c0-.6.4-1 1-1h3.5c.6 0 1 .4 1 1 0 1.3.2 2.5.6 3.6.1.3 0 .7-.2 1z"/></svg>
      (555) 284-9037
    </p>
    <p class="contact-line email">
      <svg width="34" height="24" viewBox="0 0 34 24" aria-hidden="true"><rect x="1" y="1" width="32" height="22" fill="#fff"/><path d="M1 1 L17 14 L33 1" fill="none" stroke="#050505" stroke-width="2"/></svg>
      mdelaney@brightledgerhq.example
    </p>
    <div class="base-band"></div>
  </main>
</body>
</html>
```